Event flyer for Sunday night Youth Group

Need a 4 x 6 or 5 x 7 flyer for a new youth group starting on April 14. The youth group is for students in middle school and high school so it needs to look fun and cool, but not childish. I prefer it not to include pictures of people unless it's so obscure you can't really see their faces. I've uploaded some pictures of flyers I like. I've also attached a couple versions of our logo to use on the flyer.
Information the flyer needs to include:
Youth Group
Sundays, 6-8pm (beginning April 14)
Location: Merriwick's - 4219 Hollowfern Ln S, Keizer, 97418
There will be dinner, games, friends, and a message.
Target Market(s)
Youth ages 13-18
Industry/Entity Type
Church
Colors
Designer to choose colors to be used in the design.
Look and feel

```html
<!DOCTYPE html>
<html lang="en">
<head>
<meta charset="utf-8">
<title>Youth Group Flyer</title>
<link rel="stylesheet" href="https://fonts.googleapis.com/css2?family=Montserrat:wght@400;600;700;900&family=Allura&display=swap">
<style>
  :root {
    --page-bg: #d9d7d3;
    --flyer-bg: #181616;
    --sky-dark: #231c1c;
    --sky-glow: #d9691f;
    --sky-bright: #f6c15a;
    --rust: #b5543d;
    --sage: #8fae98;
    --sage-band: #9bb3a0;
    --gold: #e8b95c;
    --ink: #151313;
    --white: #f4f1ec;
  }
  * { box-sizing: border-box; margin: 0; padding: 0; }
  html, body { width: 1200px; height: 899px; overflow: hidden; }
  body {
    background: var(--page-bg);
    font-family: "Montserrat", sans-serif;
    display: flex; align-items: center; justify-content: center;
  }
  .flyer {
    position: relative;
    width: 600px; height: 840px;
    background: var(--flyer-bg);
    overflow: hidden;
    box-shadow: 0 8px 24px rgba(0,0,0,.25);
  }
  .hero-photo {
    position: absolute; left: 0; top: 0; width: 100%; height: 460px;
    background:
      radial-gradient(ellipse 55% 30% at 50% 62%, var(--sky-bright) 0%, var(--sky-glow) 35%, rgba(120,50,20,.6) 65%, transparent 100%),
      linear-gradient(180deg, var(--sky-dark) 0%, #3a2420 40%, #2b1a17 70%, var(--flyer-bg) 100%);
  }
  .brand {
    position: absolute; top: 52px; left: 0; width: 100%;
    display: flex; flex-direction: column; align-items: center; gap: 10px;
  }
  .brand-mark { width: 34px; height: 34px; background: var(--sage); }
  .brand-name {
    color: var(--white); font-weight: 600; font-size: 17px;
    letter-spacing: 2px; text-transform: uppercase; text-align: center; line-height: 1.3;
  }
  .title-box {
    position: absolute; left: 118px; top: 428px; width: 388px; height: 128px;
    background: var(--rust);
    display: flex; align-items: center; justify-content: center;
  }
  .title-word {
    color: var(--ink); font-weight: 900; font-size: 96px; letter-spacing: 2px; line-height: 1;
  }
  .title-script {
    position: absolute; left: 0; width: 100%; top: 530px; text-align: center;
    font-family: "Allura", cursive; color: var(--sage); font-size: 120px; line-height: 1;
  }
  .schedule {
    position: absolute; top: 650px; left: 0; width: 100%; text-align: center; color: var(--white);
  }
  .schedule-day { font-weight: 700; font-size: 15px; letter-spacing: 1px; }
  .schedule-note { font-size: 10px; letter-spacing: 1px; margin-top: 2px; }
  .features {
    position: absolute; top: 700px; left: 40px; right: 40px;
    display: flex; justify-content: space-between; align-items: flex-start;
  }
  .feature { width: 110px; display: flex; flex-direction: column; align-items: center; gap: 8px; }
  .feature-icon {
    width: 52px; height: 52px; border-radius: 50%; background: var(--gold);
    display: flex; align-items: center; justify-content: center;
  }
  .feature-label { color: var(--gold); font-weight: 700; font-size: 10px; letter-spacing: 1px; }
  .divider { width: 1.5px; height: 72px; background: var(--sage); }
  .address-band {
    position: absolute; bottom: 0; left: 0; width: 100%; height: 46px;
    background: var(--sage-band);
    display: flex; align-items: center; justify-content: center;
    color: var(--ink); font-weight: 700; font-size: 14px; letter-spacing: .5px;
  }
</style>
</head>
<body>
  <main class="flyer">
    <div class="hero-photo" role="img" aria-label="Silhouettes of five young people with raised joined hands against a sunset over a city skyline"></div>

    <header class="brand">
      <div class="brand-mark"></div>
      <div class="brand-name">Waypoint Fellowship</div>
    </header>

    <div class="title-box"><span class="title-word">YOUTH</span></div>
    <div class="title-script">group</div>

    <section class="schedule">
      <p class="schedule-day">SUNDAYS, 6-8PM</p>
      <p class="schedule-note">(BEGINNING APRIL 14)</p>
    </section>

    <section class="features">
      <div class="feature">
        <div class="feature-icon">
          <svg width="30" height="30" viewBox="0 0 30 30" fill="#151313">
            <ellipse cx="10" cy="8" rx="4" ry="6"/>
            <rect x="9" y="12" width="2" height="16" rx="1"/>
            <rect x="18" y="2" width="1.5" height="9"/><rect x="21" y="2" width="1.5" height="9"/><rect x="24" y="2" width="1.5" height="9"/>
            <rect x="18" y="9" width="7.5" height="3" rx="1"/>
            <rect x="20.8" y="11" width="2" height="17" rx="1"/>
          </svg>
        </div>
        <span class="feature-label">DINNER</span>
      </div>
      <div class="divider"></div>
      <div class="feature">
        <div class="feature-icon">
          <svg width="34" height="24" viewBox="0 0 34 24" fill="none" stroke="#151313" stroke-width="2">
            <path d="M8 3h18c4 0 6 4 7 10s-1 9-4 9c-3 0-4-4-7-4h-10c-3 0-4 4-7 4s-5-3-4-9 3-10 7-10z"/>
            <path d="M9 9v6M6 12h6"/><circle cx="23" cy="10" r="1.2"/><circle cx="26" cy="13" r="1.2"/>
          </svg>
        </div>
        <span class="feature-label">GAMES</span>
      </div>
      <div class="divider"></div>
      <div class="feature">
        <div class="feature-icon">
          <svg width="32" height="26" viewBox="0 0 32 26" fill="#151313">
            <circle cx="11" cy="7" r="5"/><path d="M1 24c0-7 4-10 10-10s10 3 10 10z"/>
            <circle cx="22" cy="9" r="4"/><path d="M18 24c0-5 2-8 5-8 5 0 8 3 8 8z"/>
          </svg>
        </div>
        <span class="feature-label">FRIENDS</span>
      </div>
      <div class="divider"></div>
      <div class="feature">
        <div class="feature-icon">
          <svg width="30" height="26" viewBox="0 0 30 26" fill="#151313">
            <rect x="8" y="2" width="20" height="14" rx="2" opacity=".7"/>
            <rect x="2" y="8" width="20" height="14" rx="2"/>
          </svg>
        </div>
        <span class="feature-label">MESSAGE</span>
      </div>
    </section>

    <footer class="address-band">Merriwick's - 4219 Hollowfern Ln S, Keizer, 97418</footer>
  </main>
</body>
</html>
```